Startup online payment business - Sporting / Golf, Swift Tee payment

Background:
Our business name is "Swift Tee" we provide online payments for golfing services via our website. We currently have a logo used on our website. No other design style has been developed. Our aim is to remove cash payments for service at golf clubs.

Our Key Values:
Quick and easy
Formal and polite
Fun with professional boundary
Mate-ship relationships
100% online digital

What we want from you:
Marketing design to be used on posters and stickers in a retail setting to direct customers to our online payment Chanel.
Design must incorporate attached logo, URL swifttee.com.au and our key values can act as a guide the type of design. We have used color Hex#007672 for logo background. We are open to use other colors.

Target Market(s)

Golf clubs and golf players

Industry/Entity Type

Golf Course

Font styles to use
Sans Serif

Requirements
Must have
• Directions to online payment via URL: swifttee.com.au
Nice to have
• We like the idea of the slogan: No Cash - No worries. Have attached home screen that will be available from URL link. Consideration if using mobile phone in image. Push the online payment and steps 1. Visit swifttee.com 2. Select club 3. Confirm payment
Should not have
• Cartoons

```html
<!DOCTYPE html>
<html lang="en">
<head>
<meta charset="utf-8">
<title>Swift Tee – No Cash, No worries</title>
<link rel="stylesheet" href="https://fonts.googleapis.com/css2?family=Open+Sans:wght@400&family=Roboto:wght@400;700&display=swap">
<style>
  :root {
    --teal-light: #008a70;
    --teal-mid: #008072;
    --teal-deep: #007672;
    --white: #ffffff;
    --device-dark: #1c1c1c;
    --device-mid: #3a3a3a;
  }
  html, body {
    margin: 0;
    padding: 0;
    overflow: hidden;
  }
  .poster {
    position: relative;
    width: 1200px;
    height: 751px;
    overflow: hidden;
    color: var(--white);
    font-family: "Open Sans", sans-serif;
  }
  .backdrop {
    position: absolute;
    inset: 0;
    background: linear-gradient(160deg, var(--teal-light) 0%, var(--teal-mid) 45%, var(--teal-deep) 100%);
  }
  .brand-frame {
    position: absolute;
    left: 37px;
    top: 36px;
    width: 239px;
    height: 149px;
    border: 1.5px solid var(--white);
    box-sizing: border-box;
    text-align: center;
  }
  .brand-name {
    margin: 36px 0 0;
    font-family: "Roboto", sans-serif;
    font-weight: 700;
    font-size: 38px;
    line-height: 1;
    letter-spacing: 1px;
  }
  .brand-slogan {
    position: absolute;
    left: 0;
    right: 0;
    top: 117px;
    margin: 0;
    font-family: "Roboto", sans-serif;
    font-size: 20px;
    line-height: 1;
  }
  .web-address {
    position: absolute;
    left: 794px;
    top: 66px;
    display: flex;
    align-items: center;
    gap: 8px;
    font-family: "Roboto", sans-serif;
    font-size: 31px;
    line-height: 1;
  }
  .web-address svg {
    width: 39px;
    height: 39px;
  }
  .device-visual {
    position: absolute;
    left: 782px;
    top: 139px;
    width: 390px;
    height: 280px;
    border-radius: 6px;
    background: linear-gradient(180deg, var(--device-dark) 0%, var(--device-mid) 100%);
  }
  .values {
    position: absolute;
    left: 69px;
    top: 246px;
    margin: 0;
    padding: 0;
    list-style: none;
  }
  .values li {
    display: flex;
    align-items: center;
    height: 84px;
    font-size: 46px;
    white-space: nowrap;
  }
  .values li::before {
    content: "";
    width: 29px;
    height: 29px;
    margin-right: 23px;
    border-radius: 50%;
    background: var(--white);
    flex: none;
    transform: translateY(2px);
  }
</style>
</head>
<body>
<main class="poster">
  <div class="backdrop" role="img" aria-label="Teal background with soft diamond pattern"></div>

  <div class="brand-frame">
    <p class="brand-name">SWIFT TEE</p>
    <p class="brand-slogan">No Cash - No worries</p>
  </div>

  <div class="web-address">
    <svg viewBox="0 0 40 40" fill="none" stroke="#ffffff" stroke-width="2.6" aria-hidden="true">
      <circle cx="20" cy="20" r="17.5"/>
      <ellipse cx="20" cy="20" rx="8" ry="17.5"/>
      <line x1="20" y1="2.5" x2="20" y2="37.5"/>
      <line x1="2.5" y1="20" x2="37.5" y2="20"/>
      <path d="M5 11 H35 M5 29 H35"/>
    </svg>
    <span>www.swifttee.com.au</span>
  </div>

  <div class="device-visual" role="img" aria-label="Laptop showing the Swift Tee welcome page with a sign-up form"></div>

  <ul class="values">
    <li>Quick and easy</li>
    <li>Formal and polite</li>
    <li>Fun with professional boundary</li>
    <li>Mate-ship relationships</li>
    <li>100% online digital</li>
  </ul>
</main>
</body>
</html>
```